Brindlewood Orthopaedic logo and letterhead

Letterhead AND LOGO rediesign for a surgical medical practice located in Australia.
LOGO - should have an upper limb, shoulder, joint or convey movement
General feel is business/professional. Layout should allow as much space for text as possible
Include the information that is on the proof below that is the current letter head
Need designs in .dotx template and .pdf

Target Market(s)

general practitioner doctors

Industry/Entity Type

medical

Font styles to use
Sans Serif

Colors
0054AA
0677BA
7BADD7
CADEEF
E8F1F8

```html
<!DOCTYPE html>
<html lang="en">
<head>
<meta charset="utf-8">
<title>Brindlewood Orthopaedic – Stationery</title>
<link href="https://fonts.googleapis.com/css2?family=Montserrat:wght@400;500;600;700&family=Roboto+Condensed:wght@400;700&family=Roboto:wght@400;500&display=swap" rel="stylesheet">
<style>
  :root {
    --navy: #1b1448;
    --red: #e5252d;
    --white: #ffffff;
    --ink: #3c3c46;
    --band-top: #f4f4f6;
    --band-bottom: #c9cacd;
    --stage: #3a3b3e;
    --board: #5a5a5c;
    --ghost: #f1f1f4;
  }
  * { box-sizing: border-box; margin: 0; padding: 0; }
  html, body { width: 1200px; height: 2277px; overflow: hidden; }
  body { position: relative; background: var(--board); font-family: "Roboto", Arial, sans-serif; }

  .brand-band {
    position: absolute; left: 0; top: 0; width: 1200px; height: 143px;
    background: linear-gradient(90deg, var(--band-bottom), var(--band-top) 50%, var(--band-bottom));
    display: flex; align-items: center; justify-content: center;
  }
  .card-stage { position: absolute; left: 0; top: 143px; width: 1200px; height: 930px; background: var(--stage); }
  .stationery { position: absolute; left: 0; top: 1073px; width: 1200px; height: 1204px; background: var(--board); }

  /* Wordmark */
  .logo { display: flex; align-items: center; gap: 0.45em; font-family: "Montserrat", Arial, sans-serif; font-weight: 700; color: var(--navy); line-height: 1.05; letter-spacing: 0.06em; }
  .logo .dot { width: 1.6em; height: 1.6em; border-radius: 50%; background: currentColor; flex: none; }
  .logo.on-dark { color: var(--white); }

  /* Business cards */
  .card { position: absolute; width: 365px; height: 223px; overflow: hidden; box-shadow: 0 12px 28px rgba(0,0,0,.35); }
  .card.large { transform: scale(1.45); transform-origin: 0 0; }
  .card-front { background: var(--navy); display: flex; align-items: center; justify-content: center; }
  .card-front .logo { font-size: 17px; }
  .card-back { background: var(--white); }
  .card-back .logo { position: absolute; left: 28px; top: 26px; font-size: 11px; }
  .card-back .holder { position: absolute; right: 26px; top: 30px; text-align: right; font-family: "Montserrat", Arial, sans-serif; }
  .holder .name { font-size: 12.5px; font-weight: 500; color: var(--red); letter-spacing: .01em; }
  .holder .name b { color: var(--navy); font-weight: 700; }
  .holder .role { display: inline-block; font-size: 8px; color: #6a6a78; border-bottom: 1.5px solid var(--navy); padding-bottom: 2px; margin-top: 1px; }
  .card-back .contacts { position: absolute; left: 28px; top: 112px; list-style: none; font-size: 7.5px; color: var(--ink); }
  .contacts li { display: flex; align-items: flex-start; gap: 5px; margin-bottom: 5.5px; line-height: 1.3; }
  .icon { width: 9px; height: 9px; flex: none; }
  .card-back .rule { position: absolute; left: 0; top: 207px; width: 256px; height: 1.5px; background: var(--red); }
  .ghost-disc { position: absolute; border-radius: 50%; background: var(--ghost); }
  .card-back .ghost-disc { left: 255px; top: 88px; width: 96px; height: 96px; }

  /* Letterhead */
  .letterhead { position: absolute; left: 118px; top: 59px; width: 735px; height: 1040px; background: var(--white); box-shadow: 0 14px 34px rgba(0,0,0,.35); }
  .letterhead .logo { position: absolute; left: 24px; top: 28px; font-size: 16px; }
  .doctor { position: absolute; right: 0; top: 28px; width: 305px; font-family: "Roboto Condensed", Arial, sans-serif; }
  .doctor .name { font-size: 20.5px; font-weight: 700; color: var(--navy); }
  .doctor .credential { display: flex; align-items: center; gap: 4px; font-size: 11.5px; color: var(--red); margin-top: 2px; }
  .doctor .credential::after { content: ""; flex: 1; height: 1.5px; background: var(--navy); }
  .letterhead .ghost-disc { left: 580px; top: 880px; width: 120px; height: 120px; }
  .letter-footer { position: absolute; left: 24px; top: 937px; font-size: 13px; color: var(--ink); }
  .letter-footer .row { display: flex; align-items: center; gap: 18px; margin-bottom: 9px; }
  .letter-footer .item { display: flex; align-items: center; gap: 7px; }
  .letter-footer .icon { width: 16px; height: 16px; }
  .letter-footer .rule { width: 612px; height: 1.5px; background: var(--red); margin-left: -24px; }
  .letter-footer .note { font-family: "Montserrat", Arial, sans-serif; font-size: 12px; font-weight: 600; color: var(--navy); margin-top: 8px; }
</style>
</head>
<body>
<svg width="0" height="0" style="position:absolute" aria-hidden="true">
  <defs>
    <symbol id="ico-pin" viewBox="0 0 16 16"><rect width="16" height="16" rx="2" fill="#e5252d"/><path d="M8 3a3.2 3.2 0 0 0-3.2 3.2C4.8 8.6 8 13 8 13s3.2-4.4 3.2-6.8A3.2 3.2 0 0 0 8 3zm0 4.4a1.2 1.2 0 1 1 0-2.4 1.2 1.2 0 0 1 0 2.4z" fill="#fff"/></symbol>
    <symbol id="ico-phone" viewBox="0 0 16 16"><rect width="16" height="16" rx="2" fill="#1b1448"/><path d="M5.2 3.5l1.6 2.3-1 1.1c.6 1.3 1.6 2.3 2.9 2.9l1.1-1 2.3 1.6-.9 1.9C7.5 12.2 3.9 8.6 3.4 4.4z" fill="#fff"/></symbol>
    <symbol id="ico-fax" viewBox="0 0 16 16"><rect width="16" height="16" rx="2" fill="#1b1448"/><rect x="5" y="3" width="6" height="3" fill="#fff"/><rect x="3" y="6.5" width="10" height="5" rx="1" fill="#fff"/><rect x="5" y="9.5" width="6" height="3.5" fill="#fff" stroke="#1b1448" stroke-width=".8"/></symbol>
    <symbol id="ico-mail" viewBox="0 0 16 16"><rect width="16" height="16" rx="2" fill="#1b1448"/><rect x="3" y="4.5" width="10" height="7" fill="none" stroke="#fff" stroke-width="1.2"/><path d="M3 4.5l5 4 5-4" fill="none" stroke="#fff" stroke-width="1.2"/></symbol>
    <symbol id="ico-web" viewBox="0 0 16 16"><rect width="16" height="16" rx="2" fill="#1b1448"/><path d="M5 3v9l2.2-2 1.6 3.4 1.4-.7-1.6-3.3H11z" fill="#fff"/></symbol>
  </defs>
</svg>

<header class="brand-band">
  <div class="logo" style="font-size:20px"><span class="dot"></span><span>BRINDLEWOOD<br>ORTHOPAEDICS</span></div>
</header>

<section class="card-stage">
  <div class="card card-front large" style="left:335px; top:70px;">
    <div class="logo on-dark"><span class="dot"></span><span>BRINDLEWOOD<br>ORTHOPAEDICS</span></div>
  </div>
  <div class="card card-back large" style="left:335px; top:470px;">
    <div class="logo"><span class="dot"></span><span>BRINDLEWOOD<br>ORTHOPAEDICS</span></div>
    <div class="holder">
      <div class="name">MARTIN J. <b>ELLERY</b></div>
      <div class="role">Managing Director</div>
    </div>
    <div class="ghost-disc"></div>
    <ul class="contacts">
      <li><svg class="icon"><use href="#ico-pin"/></svg><span>Suite 4, Level 2 Eastbrook<br>Private Hospital, Kelmore Vic 3999</span></li>
      <li><svg class="icon"><use href="#ico-phone"/></svg><span>95550184</span></li>
      <li><svg class="icon"><use href="#ico-fax"/></svg><span>95550199</span></li>
      <li><svg class="icon"><use href="#ico-mail"/></svg><span>info@hargrovesurgery.com.au</span></li>
      <li><svg class="icon"><use href="#ico-web"/></svg><span>hargrovesurgery.com.au</span></li>
    </ul>
    <div class="rule"></div>
  </div>
</section>

<section class="stationery">
  <article class="letterhead">
    <div class="logo"><span class="dot"></span><span>BRINDLEWOOD<br>ORTHOPAEDICS</span></div>
    <div class="doctor">
      <div class="name">Daniel Hargrove MBBS FRACS</div>
      <div class="credential">Orthopaedic Surgeon 204417KX</div>
    </div>
    <div class="ghost-disc"></div>
    <footer class="letter-footer">
      <div class="row"><span class="item"><svg class="icon"><use href="#ico-pin"/></svg>Suite 4, Level 2 Eastbrook Private Hospital, Kelmore Vic 3999</span></div>
      <div class="row">
        <span class="item"><svg class="icon"><use href="#ico-phone"/></svg>95550184</span>
        <span class="item"><svg class="icon"><use href="#ico-fax"/></svg>95550199</span>
        <span class="item"><svg class="icon"><use href="#ico-mail"/></svg>info@hargrovesurgery.com.au</span>
      </div>
      <div class="rule"></div>
      <div class="note">We accept Corvex communication</div>
    </footer>
  </article>

  <div class="card card-front" style="left:669px; top:249px;">
    <div class="logo on-dark"><span class="dot"></span><span>BRINDLEWOOD<br>ORTHOPAEDICS</span></div>
  </div>
  <div class="card card-back" style="left:667px; top:506px;">
    <div class="logo"><span class="dot"></span><span>BRINDLEWOOD<br>ORTHOPAEDICS</span></div>
    <div class="holder">
      <div class="name">MARTIN J. <b>ELLERY</b></div>
      <div class="role">Managing Director</div>
    </div>
    <div class="ghost-disc"></div>
    <ul class="contacts">
      <li><svg class="icon"><use href="#ico-pin"/></svg><span>Suite 4, Level 2 Eastbrook<br>Private Hospital, Kelmore Vic 3999</span></li>
      <li><svg class="icon"><use href="#ico-phone"/></svg><span>95550184</span></li>
      <li><svg class="icon"><use href="#ico-fax"/></svg><span>95550199</span></li>
      <li><svg class="icon"><use href="#ico-mail"/></svg><span>info@hargrovesurgery.com.au</span></li>
      <li><svg class="icon"><use href="#ico-web"/></svg><span>hargrovesurgery.com.au</span></li>
    </ul>
    <div class="rule"></div>
  </div>
</section>
</body>
</html>
```